Sales Process Flyer

Attached is a sketch (2 pages) Id like to have a 1 page "flyer" that will explain the sales strategy for a new recruit.
Ill need to edit this down the road, so if you do it in Illustrator we will be able to handle that.
If you plenvo sales funnel you will see what im going for with the bad funnel drawing.
Id like to have icons with the text thats on the 2nd page (although it would all be 1 page)
Our brand guidelines are attached with some example pieces we have done in the past
Would like this to have an infographic type look

Something I didnt work in the sketch is below.
Estimated Sales Time:
25% - Meeting & Managing Existing Clients
25% - Free Assessments & Proposals
25% - Cold Calling
25% - New Customer Meetings & Networking

Plenvo

```html
<!DOCTYPE html>
<html lang="en">
<head>
<meta charset="utf-8">
<title>Sales Strategy</title>
<link rel="stylesheet" href="https://fonts.googleapis.com/css2?family=Barlow+Semi+Condensed:wght@500;600&family=Barlow:wght@400;600&family=Didact+Gothic&family=Gochi+Hand&display=swap">
<style>
  :root {
    --slate: #3d4f56;
    --paper: #e4eced;
    --blue: #2a9fd6;
    --blue-deep: #19688a;
    --ink: #111;
    --grey: #5a6266;
    --white: #ffffff;
  }
  * { box-sizing: border-box; margin: 0; padding: 0; }
  html, body { width: 929px; height: 1200px; overflow: hidden; }
  body { background: var(--slate); position: relative; font-family: "Barlow", sans-serif; }

  .title-panel {
    position: absolute; left: 18px; top: 8px; width: 893px; height: 104px;
    background: var(--paper);
  }
  .title {
    position: absolute; left: 0; top: -8px; width: 893px; text-align: center;
    font-family: "Barlow Semi Condensed", sans-serif; font-weight: 500;
    font-size: 124px; letter-spacing: 0; color: var(--blue); line-height: 1;
    white-space: nowrap;
  }

  .pillars {
    position: absolute; left: 18px; top: 118px; width: 893px; height: 42px;
    display: flex; font-family: "Barlow Semi Condensed", sans-serif; font-weight: 500;
    font-size: 46px; line-height: 42px; letter-spacing: 2px; white-space: nowrap;
  }
  .pillar { text-align: center; color: var(--white); }
  .pillar--strategy { width: 288px; }
  .pillar--effort { width: 303px; background: var(--blue); color: var(--paper); margin: 0 6px 0 6px; }
  .pillar--skill { flex: 1; }
  .pillar-divider { width: 4px; background: var(--white); margin-top: 2px; }

  .funnel-panel {
    position: absolute; left: 18px; top: 162px; width: 893px; height: 818px;
    background: var(--paper);
  }
  .funnel-art { position: absolute; left: 0; top: 0; }
  .stage-label {
    font-family: "Barlow", sans-serif; font-size: 26px; letter-spacing: 1px; fill: var(--white);
    text-anchor: middle;
  }

  .note {
    position: absolute; font-family: "Gochi Hand", cursive; color: var(--ink);
    font-size: 25px; line-height: 24px; text-align: center; white-space: nowrap;
  }
  .note--email { left: 30px; top: 36px; width: 330px; transform: rotate(-8deg); font-size: 30px; line-height: 25px; }
  .note--calls { left: 30px; top: 158px; width: 360px; transform: rotate(-7deg); font-size: 24px; }
  .note--activities { left: 50px; top: 296px; width: 430px; transform: rotate(3deg); font-size: 26px; }
  .note--meeting { left: 124px; top: 450px; transform: rotate(2deg); }
  .note--proposal { left: 294px; top: 562px; }
  .note--won { left: 708px; top: 728px; font-size: 40px; line-height: 40px; }

  .outcomes {
    position: absolute; left: 14px; top: 676px; list-style: none;
    font-family: "Barlow", sans-serif; font-weight: 600; font-size: 38px; letter-spacing: 1px;
    line-height: 47px; color: var(--blue); white-space: nowrap;
  }

  .activity-panel {
    position: absolute; left: 18px; top: 1000px; width: 893px; height: 184px;
    background: var(--paper); padding: 6px 12px;
  }
  .activity-list {
    list-style: none; font-family: "Didact Gothic", sans-serif; font-size: 22px;
    letter-spacing: 1px; line-height: 29px; color: var(--grey); white-space: nowrap;
  }
  .activity-list span { color: var(--blue); }
</style>
</head>
<body>
  <header class="title-panel">
    <h1 class="title">SALES STRATEGY</h1>
  </header>

  <div class="pillars">
    <div class="pillar pillar--strategy">STRATEGY</div>
    <div class="pillar-divider"></div>
    <div class="pillar pillar--effort">EFFORT</div>
    <div class="pillar-divider"></div>
    <div class="pillar pillar--skill">SKILL</div>
  </div>

  <main class="funnel-panel">
    <svg class="funnel-art" width="893" height="818" viewBox="0 0 893 818">
      <defs>
        <clipPath id="funnel-shape">
          <polygon points="350,25 879,25 614,783"/>
        </clipPath>
      </defs>
      <g clip-path="url(#funnel-shape)">
        <rect x="300" y="25" width="600" height="96" fill="var(--blue)"/>
        <rect x="300" y="121" width="600" height="112" fill="var(--blue-deep)"/>
        <rect x="300" y="233" width="600" height="98" fill="var(--blue)"/>
        <rect x="300" y="331" width="600" height="137" fill="var(--blue-deep)"/>
        <rect x="300" y="468" width="600" height="320" fill="var(--blue)"/>
      </g>
      <text class="stage-label" x="614" y="73">5% - Email Sent</text>
      <text class="stage-label" x="614" y="172">10% First Contact</text>
      <text class="stage-label" x="614" y="206">180 Goal</text>
      <text class="stage-label" x="614" y="265">25% Assessment</text>
      <text class="stage-label" x="614" y="299">60 Goal</text>
      <text class="stage-label" x="614" y="386">50% Meeting</text>
      <text class="stage-label" x="614" y="420">32 Goal</text>
      <text class="stage-label" x="614" y="524">75%</text>
      <text class="stage-label" x="614" y="558">Proposal</text>
      <text class="stage-label" x="614" y="590">16 Goal</text>

      <g fill="none" stroke="var(--ink)" stroke-width="2.5" stroke-linecap="round" stroke-linejoin="round">
        <path d="M328 86 Q355 96 384 104"/><path d="M344 73 L328 86 L346 99"/>
        <path d="M364 225 L410 206"/><path d="M372 208 L364 225 L382 231"/>
        <path d="M438 272 Q380 272 356 296"/><path d="M354 276 L356 296 L374 288"/>
        <path d="M336 460 L490 447"/><path d="M352 447 L336 460 L354 472"/>
        <path d="M420 582 L528 562"/><path d="M436 568 L420 582 L440 594"/>
        <path d="M646 750 L690 750"/><path d="M662 737 L646 750 L662 763"/>
      </g>
    </svg>

    <p class="note note--email">Landing page<br>created on website.<br>Specific email crafted.<br>500 emails sent.</p>
    <p class="note note--calls">Phone call follow up with clicks.<br>Phone call follow up with opens.<br>Phone call follow up with<br>• make free assessment</p>
    <p class="note note--activities">Run free assessments/proposals.<br>Meet/Manage existing clients<br>Cold calling<br>New customer meeting/networking</p>
    <p class="note note--meeting">Meeting scheduled</p>
    <p class="note note--proposal">Proposal</p>
    <p class="note note--won">won</p>

    <ul class="outcomes">
      <li>Lost - Price</li>
      <li>Lost - Timeline</li>
      <li>Lost - Unknown</li>
    </ul>
  </main>

  <footer class="activity-panel">
    <ul class="activity-list">
      <li>Linkora <span>- 1 hour per week prospecting and connecting</span></li>
      <li>Networking <span>- 4 events per month</span></li>
      <li>Blogging <span>- 4 posts per monthon industry specific topics</span></li>
      <li>Account Management <span>- 1 hour per week checking in with previous clients</span></li>
      <li>Trade Shows <span>- 1 per month</span></li>
      <li>Referrals <span>- Ask for referrals, generate 1 per month</span></li>
    </ul>
  </footer>
</body>
</html>
```